Velto Studio - Lash Serum Packaging

Need Packaging done for this Lash Serum for a brand called "Velto Studio". The bottle will remain black but the box can be any color. This will be for a 3ml bottle. Give me different options for packaging that is minimalist and clean for this brand that makes it look expensive and make people want to buy.

```html
<!DOCTYPE html>
<html lang="en">
<head>
<meta charset="utf-8">
<title>Velto Studio – Lash Serum Packaging</title>
<link rel="stylesheet" href="https://fonts.googleapis.com/css2?family=DM+Serif+Display&display=swap">
<style>
  :root {
    --paper: #f2efe3;
    --ink: #050505;
    --tan: #c9a684;
    --hill-dark: #0c0a08;
    --hill-warm: #2a2117;
  }
  * { margin: 0; padding: 0; box-sizing: border-box; }
  html, body { width: 1200px; height: 2393px; overflow: hidden; }
  body {
    background: var(--paper);
    position: relative;
    font-family: "DM Serif Display", Georgia, serif;
  }
  .panel {
    position: absolute;
    background: var(--ink);
    color: var(--tan);
    overflow: hidden;
  }
  .box-front { left: 202px; top: 719px; width: 288px; height: 954px; }
  .bottle-label { left: 573px; top: 1029px; width: 425px; height: 644px; border-top: 8px solid var(--tan); }

  .brand-tag {
    position: absolute;
    font-size: 13px;
    letter-spacing: 1px;
    white-space: nowrap;
    color: var(--tan);
  }
  .box-front .brand-tag { left: 0; right: 0; top: 30px; text-align: center; }
  .bottle-label .brand-tag { right: 48px; top: 44px; }

  .brand-name {
    position: absolute;
    writing-mode: vertical-rl;
    text-transform: lowercase;
    line-height: 1;
    white-space: nowrap;
    color: var(--tan);
  }
  .box-front .brand-name { left: 100px; top: 178px; font-size: 84px; }
  .bottle-label .brand-name { left: 58px; top: 120px; font-size: 54px; }

  .hills {
    position: absolute;
    left: 0; right: 0; bottom: 0;
    background: linear-gradient(180deg, var(--hill-dark) 0%, var(--hill-warm) 55%, var(--hill-dark) 100%);
  }
  .box-front .hills { top: 634px; }
  .bottle-label .hills { top: 432px; }

  .volume {
    position: absolute;
    left: 70px; bottom: 14px;
    font-size: 13px;
    font-style: italic;
    color: var(--tan);
  }
</style>
</head>
<body>
  <section class="panel box-front">
    <div class="brand-tag">Velto Studio</div>
    <h1 class="brand-name">Velto Studio</h1>
    <div class="hills" role="img" aria-label="Fine tan line drawing of rolling hills and flowing dunes"></div>
  </section>

  <section class="panel bottle-label">
    <div class="brand-tag">Velto Studio</div>
    <h2 class="brand-name">Velto Studio</h2>
    <div class="hills" role="img" aria-label="Fine tan line drawing of rolling hills and flowing dunes"></div>
    <span class="volume">3ml</span>
  </section>
</body>
</html>
```